Smack you in the face - Landing page for Residential Electrical Repairs (Searchly Ads)

I need an effective landing page for Searchly ads. The ads will target residential electrical repairs. Lighting Outages, Power Outages, Breakers Tripping, Outlets Not Working. I need a strong call to action to Call Us Now! Forms don't work well for us so we only need one form as a last option at the bottom of the page. We only work on homes. the website is https://www.keystone-wiring.com/
email is : support@keystone-wiring.com
Phone 864-555-0172

**This is about one focused service. Electrical Repairs - That includes Partial Power Outages, Outlets Not Working, Tripped Breakers, Electrical Panel repairs, and Fusebox Repairs. The area served will only be Greenville, SC. VIMO is the platform

Target Market(s)

Homeonwers in need of electrical repair

Industry/Entity Type

Residential Electricians

Coding

Coded - Design and coding required

Requirements
Must have
• Strong to action for phone calls, this landing page must grab action fast.
Nice to have
• Social proof with existing 5 start reviews for Searchly, Rateo, TFC, and Friendhub
Should not have
• Should not be form based. I do not like the site's current them, please don't copy it. Make your own.

```html
<!DOCTYPE html>
<html lang="en">
<head>
<meta charset="utf-8">
<title>Keystone Wiring – Emergency Electrical Repairs in Greenville, SC</title>
<link href="https://fonts.googleapis.com/css2?family=Outfit:wght@300;400;500;600&display=swap" rel="stylesheet">
<style>
  :root{
    --brand-blue:#2a93c9;
    --brand-navy:#12284a;
    --ink:#111111;
    --paper:#ffffff;
    --band:rgba(0,0,0,.82);
    --band-blue:rgba(10,110,170,.82);
    --overlay:#175f9a;
    --footer:#000000;
    --star-bg:#10345c;
    --star:#f5c518;
  }
  *{box-sizing:border-box;margin:0;padding:0}
  html,body{width:686px;height:1200px;overflow:hidden}
  body{font-family:'Outfit',sans-serif;color:var(--ink);background:var(--paper);position:relative}
  .abs{position:absolute}

  /* header */
  .site-header{left:0;top:0;width:686px;height:51px;background:var(--paper)}
  .brand{display:flex;align-items:center;gap:4px;font-weight:600;font-size:10px;letter-spacing:.5px;color:var(--brand-navy)}
  .brand-dot{width:8px;height:8px;border-radius:50%;background:var(--brand-blue)}
  .site-header .brand{position:absolute;left:23px;top:19px}
  .nav{position:absolute;left:141px;top:21px;display:flex;gap:10px;font-size:7.6px;list-style:none;color:var(--ink)}
  .nav .current{color:var(--brand-blue)}
  .header-phone{position:absolute;left:548px;top:20px;display:flex;align-items:center;gap:6px;font-size:8.6px}

  /* hero */
  .hero{left:0;top:51px;width:686px;height:211px;overflow:hidden}
  .hero-photo{position:absolute;top:0;height:211px}
  .hero-photo.meter{left:0;width:220px;background:linear-gradient(135deg,#d8dcdf,#8b949b 60%,#3c4a52)}
  .hero-photo.tech{left:221px;width:248px;background:linear-gradient(135deg,#eceae6,#c2b8ac 40%,#3d6db4 80%,#2b3040)}
  .hero-photo.breaker{left:470px;width:216px;background:linear-gradient(135deg,#6c7076,#2d3034 60%,#c9c2b8)}
  .hero-band{position:absolute;left:0;top:107px;width:686px;height:85px;background:linear-gradient(90deg,var(--band-blue) 0,var(--band-blue) 33%,var(--band) 60%)}
  .hero-title{position:absolute;left:0;width:686px;top:112px;text-align:center;color:#fff;font-size:26.5px;font-weight:400}
  .hero-call{position:absolute;left:0;width:686px;top:152px;text-align:center;color:#fff;font-size:21px;font-style:italic;font-weight:300}
  .hero-call b{font-weight:500;margin-left:14px}

  /* intro */
  .intro-text{left:24px;top:285px;width:270px;font-size:11px;line-height:17.2px;color:var(--brand-blue);font-weight:300}
  .btn{display:flex;align-items:center;justify-content:center;background:#000;color:#fff;font-size:14px;letter-spacing:1.2px;font-weight:500;border-radius:2px}
  .btn-services{left:23px;top:372px;width:180px;height:25px}
  .btn-quote{left:527px;top:373px;width:128px;height:25px}
  .problems-title{left:358px;top:282px;font-size:14.3px;font-weight:300}
  .problems{left:358px;top:306px;list-style:none;font-size:10.8px;font-weight:500;color:var(--brand-blue)}
  .problems li{height:19.4px;display:flex;align-items:center;gap:10px}
  .problems li::before{content:"";width:6px;height:6px;border-radius:50%;background:var(--brand-blue)}

  /* testimonials */
  .section-title{left:0;width:686px;top:426px;text-align:center;font-size:27.5px;font-weight:300}
  .rule{top:473px;height:2px;background:var(--brand-blue)}
  .rule.left{left:23px;width:310px}
  .rule.right{left:356px;width:309px}
  .review-photo{top:502px;width:98px;height:98px}
  .review-photo.one{left:48px;background:linear-gradient(160deg,#9aa3a8,#6f7f8c 60%,#b9c9d8)}
  .review-photo.two{left:383px;background:linear-gradient(160deg,#f1c6d4,#e7b4c4 55%,#b7d764)}
  .review-name{top:500px;font-size:14px;font-weight:300}
  .review-text{top:530px;width:140px;font-size:9.6px;line-height:11px;font-weight:300}
  .stars{top:640px;display:flex;gap:0;height:11px;background:var(--star-bg);padding:0 2px}
  .stars svg{width:15.5px;height:11px}

  /* contact */
  .contact{left:0;top:684px;width:686px;height:374px;background:linear-gradient(180deg,#1d6aa6,#14568d)}
  .contact-divider{left:321px;top:714px;width:3px;height:318px;background:#fff}
  .contact-headline{left:0;width:308px;top:800px;text-align:center;color:#fff;font-size:29px;line-height:30px;font-weight:300}
  .contact-cta{left:0;width:316px;top:888px;text-align:center;color:#fff;font-size:29px;font-weight:300}
  .form-label{width:150px;left:291px;text-align:right;color:#fff;font-size:18.5px;font-weight:300}
  .field{left:453px;width:180px;border:1.5px solid #fff}
  .btn-send{left:454px;top:942px;width:94px;height:25px;font-size:14px}

  /* footer */
  .site-footer{left:0;top:1058px;width:686px;height:142px;background:var(--footer)}
  .site-footer .brand{position:absolute;left:36px;top:52px;color:#fff;font-size:11px}
  .footer-line{display:flex;align-items:center;gap:10px;color:#fff;font-size:14px;font-weight:300;position:absolute;left:293px}
  .social{position:absolute;top:40px;width:30px;height:30px;border-radius:50%;background:#fff;color:#000;font-size:5.4px;display:flex;align-items:center;justify-content:center;font-weight:500}
</style>
</head>
<body>

<header class="site-header abs">
  <div class="brand"><span class="brand-dot"></span>KEYSTONE WIRING</div>
  <ul class="nav">
    <li class="current">HOME</li><li>SERVICES⌄</li><li>ABOUT</li><li>EMPLOYMENT</li><li>BLOG</li><li>CONTACT</li><li>AREAS WE SERVE⌄</li>
  </ul>
  <div class="header-phone">
    <svg width="10" height="10" viewBox="0 0 24 24"><path d="M6.6 10.8a15 15 0 0 0 6.6 6.6l2.2-2.2a1 1 0 0 1 1-.25 11.4 11.4 0 0 0 3.6.6 1 1 0 0 1 1 1V20a1 1 0 0 1-1 1A17 17 0 0 1 3 4a1 1 0 0 1 1-1h3.5a1 1 0 0 1 1 1c0 1.25.2 2.45.6 3.6a1 1 0 0 1-.25 1z" fill="#111"/></svg>
    (864) 555-0172
  </div>
</header>

<section class="hero abs">
  <div class="hero-photo meter" role="img" aria-label="Hands testing a wall outlet with a multimeter"></div>
  <div class="hero-photo tech" role="img" aria-label="Smiling technician in a cap working on a breaker panel"></div>
  <div class="hero-photo breaker" role="img" aria-label="Close-up of circuit breakers in a panel"></div>
  <div class="hero-band"></div>
  <h1 class="hero-title">Your electrical emergency is our urgency!</h1>
  <p class="hero-call">Call now! <b>(864) 555-0172</b></p>
</section>

<p class="intro-text abs">We have Licensed Electricians in Greenville, SC ensuring top-tier service for every call. We've built our reputation as the go-to Emergency Electrician for homeowners in need.</p>
<div class="btn btn-services abs">VIEW ALL SERVICES</div>

<h2 class="problems-title abs">Are you experiencing electrical problems like:</h2>
<ul class="problems abs">
  <li>Partial Power Outages</li>
  <li>Outlets Not Working</li>
  <li>Tripped Breakers</li>
  <li>Electrical Panel repairs</li>
  <li>Fusebox Repairs</li>
</ul>
<div class="btn btn-quote abs">GET A QUOTE</div>

<h2 class="section-title abs">Testimonials</h2>
<div class="rule left abs"></div>
<div class="rule right abs"></div>

<div class="review-photo one abs" role="img" aria-label="Portrait of customer Dalton P."></div>
<h3 class="review-name abs" style="left:176px">Dalton P.</h3>
<p class="review-text abs" style="left:177px">Lorem ipsum dolor sit amet, consectetur adipiscing elit, sed do eiusmod tempor incididunt ut labore et dolore magna aliqua. Quis ipsum suspendisse ultrices gravida. Risus commodo viverra maecenas accumsan lacus vel facilisis.</p>
<div class="stars abs" style="left:177px" aria-label="5 stars">
  <svg viewBox="0 0 16 11"><polygon points="8,1.5 9.3,4.6 12.6,4.8 10,6.9 10.9,10 8,8.2 5.1,10 6,6.9 3.4,4.8 6.7,4.6" fill="var(--star)"/></svg>
  <svg viewBox="0 0 16 11"><polygon points="8,1.5 9.3,4.6 12.6,4.8 10,6.9 10.9,10 8,8.2 5.1,10 6,6.9 3.4,4.8 6.7,4.6" fill="var(--star)"/></svg>
  <svg viewBox="0 0 16 11"><polygon points="8,1.5 9.3,4.6 12.6,4.8 10,6.9 10.9,10 8,8.2 5.1,10 6,6.9 3.4,4.8 6.7,4.6" fill="var(--star)"/></svg>
  <svg viewBox="0 0 16 11"><polygon points="8,1.5 9.3,4.6 12.6,4.8 10,6.9 10.9,10 8,8.2 5.1,10 6,6.9 3.4,4.8 6.7,4.6" fill="var(--star)"/></svg>
  <svg viewBox="0 0 16 11"><polygon points="8,1.5 9.3,4.6 12.6,4.8 10,6.9 10.9,10 8,8.2 5.1,10 6,6.9 3.4,4.8 6.7,4.6" fill="var(--star)"/></svg>
</div>

<div class="review-photo two abs" role="img" aria-label="Portrait of customer Maren T."></div>
<h3 class="review-name abs" style="left:511px">Maren T.</h3>
<p class="review-text abs" style="left:512px">Lorem ipsum dolor sit amet, consectetur adipiscing elit, sed do eiusmod tempor incididunt ut labore et dolore magna aliqua. Quis ipsum suspendisse ultrices gravida. Risus commodo viverra maecenas accumsan lacus vel facilisis.</p>
<div class="stars abs" style="left:512px" aria-label="5 stars">
  <svg viewBox="0 0 16 11"><polygon points="8,1.5 9.3,4.6 12.6,4.8 10,6.9 10.9,10 8,8.2 5.1,10 6,6.9 3.4,4.8 6.7,4.6" fill="var(--star)"/></svg>
  <svg viewBox="0 0 16 11"><polygon points="8,1.5 9.3,4.6 12.6,4.8 10,6.9 10.9,10 8,8.2 5.1,10 6,6.9 3.4,4.8 6.7,4.6" fill="var(--star)"/></svg>
  <svg viewBox="0 0 16 11"><polygon points="8,1.5 9.3,4.6 12.6,4.8 10,6.9 10.9,10 8,8.2 5.1,10 6,6.9 3.4,4.8 6.7,4.6" fill="var(--star)"/></svg>
  <svg viewBox="0 0 16 11"><polygon points="8,1.5 9.3,4.6 12.6,4.8 10,6.9 10.9,10 8,8.2 5.1,10 6,6.9 3.4,4.8 6.7,4.6" fill="var(--star)"/></svg>
  <svg viewBox="0 0 16 11"><polygon points="8,1.5 9.3,4.6 12.6,4.8 10,6.9 10.9,10 8,8.2 5.1,10 6,6.9 3.4,4.8 6.7,4.6" fill="var(--star)"/></svg>
</div>

<section class="contact abs" role="img" aria-label="Team of electricians standing in front of a company service van, tinted blue"></section>
<div class="contact-divider abs"></div>
<h2 class="contact-headline abs">Your Electrical Needs,<br>Our Expertise.</h2>
<p class="contact-cta abs">Contact Us!</p>

<label class="form-label abs" style="top:808px">Name</label>
<label class="form-label abs" style="top:833px">Email</label>
<label class="form-label abs" style="top:859px">Phone</label>
<label class="form-label abs" style="top:884px">Message</label>
<div class="field abs" style="top:812px;height:21px"></div>
<div class="field abs" style="top:836px;height:21px"></div>
<div class="field abs" style="top:862px;height:21px"></div>
<div class="field abs" style="top:888px;height:48px;left:454px"></div>
<div class="btn btn-send abs">SEND</div>

<footer class="site-footer abs">
  <div class="brand"><span class="brand-dot"></span>KEYSTONE WIRING</div>
  <div class="footer-line" style="top:36px">
    <svg width="14" height="20" viewBox="0 0 14 20"><path d="M7 0a7 7 0 0 0-7 7c0 5 7 13 7 13s7-8 7-13a7 7 0 0 0-7-7zm0 9.5A2.5 2.5 0 1 1 7 4.5a2.5 2.5 0 0 1 0 5z" fill="#fff"/></svg>
    218 Harlow Ave, STE 4
  </div>
  <div class="footer-line" style="top:66px">
    <svg width="15" height="15" viewBox="0 0 24 24"><path d="M6.6 10.8a15 15 0 0 0 6.6 6.6l2.2-2.2a1 1 0 0 1 1-.25 11.4 11.4 0 0 0 3.6.6 1 1 0 0 1 1 1V20a1 1 0 0 1-1 1A17 17 0 0 1 3 4a1 1 0 0 1 1-1h3.5a1 1 0 0 1 1 1c0 1.25.2 2.45.6 3.6a1 1 0 0 1-.25 1z" fill="#fff"/></svg>
    (864) 555-0172
  </div>
  <div class="social" style="left:524px">Friendhub</div>
  <div class="social" style="left:567px">Chirper</div>
  <div class="social" style="left:611px">Linkwork</div>
</footer>

</body>
</html>
```